Business card for event manager / organizer "velmora tandem"

Draft of a new valuable business card for my company.
Events, personnel service providers, festivals

```html
<!DOCTYPE html>
<html lang="de">
<head>
<meta charset="utf-8">
<title>velmora tandem – Visitenkarte</title>
<link rel="stylesheet" href="https://fonts.googleapis.com/css2?family=Roboto:wght@300;400;500;700&family=Roboto+Condensed:wght@700&display=swap">
<style>
  :root {
    --backdrop: #8f8f8f;
    --paper: #ffffff;
    --paper-shade: #eeeeee;
    --ink: #111111;
    --gold: #b8975a;
    --card-black: #050505;
    --muted: #9a9a9a;
    --photo-dark: #1a1a1a;
    --photo-mid: #5a5a62;
  }
  * { margin: 0; padding: 0; box-sizing: border-box; }
  html, body {
    width: 1200px; height: 1056px; overflow: hidden;
    background: var(--backdrop);
    font-family: "Roboto", Arial, sans-serif;
  }
  .stage { position: relative; width: 1200px; height: 1056px; }
  .card {
    position: absolute; left: 270px; width: 660px; height: 400px;
    border-radius: 3px; overflow: hidden;
    box-shadow: 0 18px 30px rgba(0,0,0,.28);
  }
  /* front */
  .card--front {
    top: 90px;
    background: linear-gradient(160deg, var(--paper) 40%, var(--paper-shade) 100%);
  }
  .holder { position: absolute; left: 48px; top: 50px; }
  .holder__name {
    color: var(--gold); font-weight: 700; font-size: 38px; letter-spacing: .2px;
  }
  .holder__role {
    color: var(--ink); font-weight: 700; font-size: 19px; margin-top: 2px;
    padding-bottom: 10px; width: 180px; border-bottom: 2px solid var(--ink);
  }
  .contact {
    position: absolute; left: 48px; top: 212px; list-style: none;
    font-size: 15px; color: var(--ink); line-height: 24px;
  }
  .contact li { display: flex; align-items: center; gap: 9px; }
  .contact svg { width: 15px; height: 15px; flex: none; }
  .portrait {
    position: absolute; right: 0; bottom: 0; width: 260px; height: 290px;
    background: radial-gradient(ellipse at 60% 30%, var(--photo-mid) 0%, var(--photo-dark) 70%);
    clip-path: polygon(8% 32%, 60% 0, 100% 5%, 100% 100%, 0 100%, 3% 70%);
  }
  /* back */
  .card--back { top: 560px; background: var(--card-black); color: #fff; }
  .brand {
    position: absolute; left: 0; right: 0; top: 128px;
    display: flex; justify-content: center; align-items: center; gap: 18px;
  }
  .brand__mark { width: 70px; height: 70px; background: var(--gold); }
  .brand__name {
    font-family: "Roboto Condensed", Arial, sans-serif; font-weight: 700;
    font-size: 52px; text-transform: uppercase; color: #fff; letter-spacing: .5px;
  }
  .tagline {
    position: absolute; left: 0; right: 0; top: 214px; text-align: center;
    color: var(--muted); font-size: 13px; font-weight: 300;
  }
  .services {
    position: absolute; left: 0; right: 0; top: 300px; text-align: center;
    font-family: "Roboto Condensed", Arial, sans-serif; font-weight: 700;
    font-size: 22px; letter-spacing: .3px;
  }
  .services .dot { color: var(--gold); margin: 0 8px; }
</style>
</head>
<body>
<main class="stage">
  <section class="card card--front">
    <div class="holder">
      <div class="holder__name">Jonas Berlinger</div>
      <div class="holder__role">Inhaber</div>
    </div>
    <ul class="contact">
      <li><svg viewBox="0 0 16 16"><circle cx="8" cy="8" r="8" fill="#b8975a"/><path d="M5 4.5l1.6-.4 1 2-1 .8c.5 1.1 1.3 1.9 2.4 2.4l.8-1 2 1-.4 1.6c-3.3 0-6.4-3.1-6.4-6.4z" fill="#fff"/></svg>02361 555 01 23</li>
      <li><svg viewBox="0 0 16 16"><circle cx="8" cy="8" r="8" fill="#b8975a"/><path d="M5 4.5l1.6-.4 1 2-1 .8c.5 1.1 1.3 1.9 2.4 2.4l.8-1 2 1-.4 1.6c-3.3 0-6.4-3.1-6.4-6.4z" fill="#fff"/></svg>0170 555 42 18</li>
      <li><svg viewBox="0 0 16 16"><circle cx="8" cy="8" r="8" fill="#b8975a"/><g fill="none" stroke="#fff" stroke-width=".9"><circle cx="8" cy="8" r="4.3"/><ellipse cx="8" cy="8" rx="1.8" ry="4.3"/><path d="M3.7 8h8.6"/></g></svg>www.velmora-tandem.de</li>
      <li><svg viewBox="0 0 16 16"><circle cx="8" cy="8" r="8" fill="#b8975a"/><rect x="4" y="5.2" width="8" height="5.6" fill="#fff"/><path d="M4 5.2l4 3 4-3" fill="none" stroke="#b8975a" stroke-width=".9"/></svg>info@velmora-tandem.de</li>
      <li><svg viewBox="0 0 16 16"><circle cx="8" cy="8" r="8" fill="#b8975a"/><path d="M8 3.5a3 3 0 0 1 3 3c0 2.2-3 6-3 6s-3-3.8-3-6a3 3 0 0 1 3-3z" fill="#fff"/><circle cx="8" cy="6.5" r="1.1" fill="#b8975a"/></svg>Lindenweg 14, 45699 Herten</li>
      <li><svg viewBox="0 0 16 16"><circle cx="8" cy="8" r="8" fill="#b8975a"/></svg>social.velmora-tandem.de/team</li>
    </ul>
    <div class="portrait" role="img" aria-label="Porträtfoto des Inhabers in Weste vor schwarzem Pinselstrich"></div>
  </section>

  <section class="card card--back">
    <div class="brand">
      <span class="brand__mark"></span>
      <span class="brand__name">velmora tandem</span>
    </div>
    <p class="tagline">…weil jedes Fest gute Hände verdient!</p>
    <p class="services">EVENTS<span class="dot">•</span>PERSONNEL SERVICE PROVIDERS<span class="dot">•</span>FESTIVALS</p>
  </section>
</main>
</body>
</html>
```